Veterinary Business cards

Redesign Business Card

Information needed on Card:
Hours: Mon-Fri: 4pm -10PM; Sat- Sun- 10 AM- 5PM
Help@tandrelyns.com
www.tandrelyns.com
405-718-2954
4170 SW 38th Ave. okc, ok 73119
*No appointment necessary*

Optional:
Our tag line is "We're here when you need us" - If it fits on the cards.

```html
<!DOCTYPE html>
<html lang="en">
<head>
<meta charset="utf-8">
<title>Tandrelyn's Urgent Care – Business Cards</title>
<link rel="stylesheet" href="https://fonts.googleapis.com/css2?family=Archivo+Black&family=Arimo:wght@400;700&display=swap">
<style>
  :root {
    --navy: #1b3d69;
    --navy-soft: #22487a;
    --orange: #d77b1e;
    --white: #ffffff;
    --backdrop: #2a2a2c;
  }
  * { box-sizing: border-box; margin: 0; padding: 0; }
  html, body { width: 1200px; height: 1015px; overflow: hidden; }
  body {
    background: var(--backdrop);
    font-family: "Arimo", Arial, sans-serif;
    display: flex;
    flex-direction: column;
    align-items: center;
    justify-content: center;
    gap: 48px;
  }
  .card {
    position: relative;
    width: 700px;
    height: 400px;
    background: var(--navy);
    overflow: hidden;
    box-shadow: 0 10px 24px rgba(0,0,0,0.55);
  }
  .card__band {
    position: absolute;
    left: 0; right: 0; bottom: 0;
    height: 64px;
    background: var(--orange);
    display: flex;
    align-items: center;
    color: var(--white);
  }

  /* Front */
  .brand {
    position: absolute;
    left: 0; right: 0; top: 130px;
    display: flex;
    align-items: center;
    justify-content: center;
    gap: 18px;
    color: var(--white);
  }
  .brand__mark {
    width: 44px;
    height: 44px;
    border-radius: 50%;
    background: var(--orange);
    flex: none;
  }
  .brand__name {
    font-family: "Arimo", Arial, sans-serif;
    font-weight: 400;
    font-size: 44px;
    line-height: 1.1;
  }
  .tagline-band { justify-content: center; }
  .tagline {
    font-family: "Archivo Black", "Arial Black", sans-serif;
    font-size: 24px;
    letter-spacing: 2px;
    text-transform: uppercase;
  }

  /* Back */
  .details {
    position: absolute;
    left: 60px;
    top: 120px;
    color: var(--white);
    font-size: 21px;
    line-height: 1.28;
  }
  .details__label {
    color: var(--orange);
    font-weight: 700;
    font-size: 23px;
  }
  .details__hours { margin-left: 18px; }
  .details__note {
    margin-left: 18px;
    margin-top: 4px;
    color: var(--orange);
    font-weight: 700;
    font-size: 18px;
  }
  .contact {
    list-style: none;
    margin-top: 14px;
    margin-left: 34px;
  }
  .contact li {
    display: flex;
    align-items: center;
    gap: 10px;
  }
  .contact svg { width: 18px; height: 18px; flex: none; }
  .address-band {
    justify-content: flex-end;
    gap: 10px;
    padding-right: 60px;
    font-size: 22px;
  }
  .address-band svg { width: 18px; height: 24px; flex: none; }
</style>
</head>
<body>

  <section class="card card--front" aria-label="Card front">
    <div class="brand">
      <span class="brand__mark" aria-hidden="true"></span>
      <span class="brand__name">Tandrelyn's Urgent Care</span>
    </div>
    <div class="card__band tagline-band">
      <span class="tagline">We're here when you need us</span>
    </div>
  </section>

  <section class="card card--back" aria-label="Card back">
    <div class="details">
      <div class="details__label">Hours:</div>
      <div class="details__hours">Mon-Fri: 4pm -10PM;<br>Sat- Sun- 10 AM- 5PM</div>
      <div class="details__note">*No appointment necessary*</div>
      <ul class="contact">
        <li>
          <svg viewBox="0 0 24 24" aria-hidden="true"><path fill="var(--orange)" d="M6.6 10.8a15 15 0 0 0 6.6 6.6l2.2-2.2a1 1 0 0 1 1-.25 11.4 11.4 0 0 0 3.6.57 1 1 0 0 1 1 1V20a1 1 0 0 1-1 1A17 17 0 0 1 3 4a1 1 0 0 1 1-1h3.5a1 1 0 0 1 1 1c0 1.25.2 2.45.57 3.57a1 1 0 0 1-.25 1z"/></svg>
          405-718-2954
        </li>
        <li>
          <svg viewBox="0 0 24 24" aria-hidden="true"><rect x="2" y="5" width="20" height="14" fill="var(--orange)"/><path d="M2 5l10 8 10-8" fill="none" stroke="var(--navy)" stroke-width="2"/></svg>
          Help@tandrelyns.com
        </li>
        <li>
          <svg viewBox="0 0 24 24" aria-hidden="true"><g fill="none" stroke="var(--orange)" stroke-width="2"><circle cx="12" cy="12" r="9"/><ellipse cx="12" cy="12" rx="4" ry="9"/><path d="M3 12h18M5 7h14M5 17h14"/></g></svg>
          www.tandrelyns.com
        </li>
      </ul>
    </div>
    <div class="card__band address-band">
      <svg viewBox="0 0 18 24" aria-hidden="true"><path fill="var(--white)" d="M9 0a9 9 0 0 0-9 9c0 6.5 9 15 9 15s9-8.5 9-15a9 9 0 0 0-9-9zm0 12.5A3.5 3.5 0 1 1 9 5.5a3.5 3.5 0 0 1 0 7z"/></svg>
      4170 SW 38th Ave. okc, ok 73119
    </div>
  </section>

</body>
</html>
```